Tr construction holdings pty ltd

2 sided card black and red with white
Very professional and elegant

Target Market(s)

Construction and Development

Industry/Entity Type

Construction and development

Contact Information for Business Card

One side black, one side red/or white business logo in top corner, email: morgan@trbuildworks.example

Requirements
Should not have
• Blue

```html
<!DOCTYPE html>
<html lang="en">
<head>
<meta charset="utf-8">
<title>TR Construction – Business Card</title>
<link href="https://fonts.googleapis.com/css2?family=Open+Sans:wght@400;600;700&display=swap" rel="stylesheet">
<style>
  :root {
    --stage: #3f3f3f;
    --card: #1c1c1c;
    --card-dark: #181818;
    --red: #e0291a;
    --white: #f2f2f2;
    --grey: #d6d6d6;
    --emboss: #0b0b0b;
  }
  * { box-sizing: border-box; margin: 0; padding: 0; }
  html, body { width: 1200px; height: 1050px; overflow: hidden; }
  body {
    background: var(--stage);
    font-family: "Open Sans", sans-serif;
    display: flex;
    flex-direction: column;
    align-items: center;
    justify-content: center;
    gap: 48px;
  }
  .card {
    position: relative;
    width: 760px;
    height: 434px;
    background: var(--card);
    overflow: hidden;
  }
  .card--front { border: 2px solid var(--red); }
  .card--back {
    background: var(--card-dark);
    border-bottom: 8px solid var(--red);
  }

  .wordmark {
    display: flex;
    align-items: center;
    gap: 8px;
    font-weight: 700;
    letter-spacing: 0.06em;
    text-transform: uppercase;
  }
  .wordmark__dot {
    width: 10px; height: 10px; border-radius: 50%;
    background: var(--red);
    margin-top: 16px;
  }
  .card--front .wordmark {
    position: absolute; left: 64px; top: 66px;
    font-size: 36px; color: var(--white);
  }
  .card--back .wordmark {
    position: absolute; left: 50%; top: 50%;
    transform: translate(-50%, -50%);
    font-size: 52px; color: var(--emboss);
  }
  .card--back .wordmark__dot { background: var(--emboss); width: 13px; height: 13px; margin-top: 26px; }

  .divider {
    position: absolute; left: 70px; top: 200px;
    width: 400px; height: 1px; background: var(--red);
  }
  .contacts {
    position: absolute; left: 60px; top: 214px;
    list-style: none;
    font-size: 16px; color: var(--grey);
    line-height: 28px;
  }
  .contacts li { display: flex; align-items: center; gap: 10px; }
  .contacts svg { width: 14px; height: 14px; flex: none; }

  .person {
    position: absolute; right: 56px; top: 166px;
    text-align: right;
  }
  .person__name {
    font-size: 30px; font-weight: 600; color: var(--red);
    letter-spacing: 0.04em; line-height: 1.1;
  }
  .person__title {
    font-size: 17px; font-weight: 600; color: var(--grey);
    letter-spacing: 0.03em; margin-top: 4px;
  }
  .address {
    position: absolute; right: 56px; top: 280px;
    text-align: right;
    font-size: 17px; color: var(--grey);
    line-height: 30px; letter-spacing: 0.03em;
  }
</style>
</head>
<body>

  <section class="card card--front">
    <div class="wordmark"><span>TR Construction</span><span class="wordmark__dot"></span></div>

    <div class="divider"></div>

    <ul class="contacts">
      <li>
        <svg viewBox="0 0 16 16" aria-hidden="true"><path fill="#e0291a" d="M4 1l3 3-1.6 2a9 9 0 0 0 4.6 4.6L12 9l3 3-2 2.5C7 14 2 9 1.5 3z"/></svg>
        (123)456-7891
      </li>
      <li>
        <svg viewBox="0 0 16 16" aria-hidden="true"><rect x="1" y="3" width="14" height="10" fill="#e0291a"/><path d="M1 3l7 6 7-6" stroke="#1c1c1c" stroke-width="1.4" fill="none"/></svg>
        morgan@trbuildworks.example
      </li>
      <li>
        <svg viewBox="0 0 16 16" aria-hidden="true"><circle cx="8" cy="8" r="7" fill="#e0291a"/><path d="M1 8h14M8 1c-3 3-3 11 0 14M8 1c3 3 3 11 0 14" stroke="#1c1c1c" stroke-width="1" fill="none"/></svg>
        www.trbuildworks.example
      </li>
    </ul>

    <div class="person">
      <p class="person__name">JOHN SMITH</p>
      <p class="person__title">Managing Director</p>
    </div>

    <p class="address">P.O. Box 000. Postal Code 00<br>Your City, Country</p>
  </section>

  <section class="card card--back">
    <div class="wordmark"><span>TR Construction</span><span class="wordmark__dot"></span></div>
  </section>

</body>
</html>
```